Business Card Design

as above
one side to be name of business and information about business inside an imessage text bubble.
other side to be contact details around an email icon . 'envelope'

Target Market(s)

seniors

Industry/Entity Type

Business

Contact Information for Business Card

Tech Along-Keep Along
Marlene Hobb
0461 837 204
Marlene.techalong@quillmail.test
ABN:74618250913

Technology help for seniors in your own home.- ipads, ipods, mobile phones, internet, email, computers. No question too small.

```html
<!DOCTYPE html>
<html lang="en">
<head>
<meta charset="utf-8">
<title>Tech Along, Keep Along – Business Card</title>
<link rel="stylesheet" href="https://fonts.googleapis.com/css2?family=Chewy&family=Fredoka:wght@600&family=Oswald:wght@700&display=swap">
<style>
  :root {
    --page: #ffffff;
    --frame: #1a2fd0;
    --code-dark: #0a2258;
    --code-mid: #2f5fa6;
    --code-light: #7fa6d8;
    --ink: #000000;
    --cloud: #ffffff;
    --word: #5cc8f2;
  }
  html, body {
    margin: 0;
    width: 1200px;
    height: 741px;
    overflow: hidden;
    background: var(--page);
  }
  .card {
    display: block;
    width: 1200px;
    height: 741px;
  }
  .headline {
    font-family: "Chewy", "Fredoka", sans-serif;
    fill: var(--cloud);
    stroke: var(--ink);
    stroke-width: 8px;
    paint-order: stroke fill;
    stroke-linejoin: round;
  }
  .service {
    font-family: "Oswald", sans-serif;
    font-weight: 700;
    fill: var(--word);
    stroke: var(--ink);
    stroke-width: 3px;
    paint-order: stroke fill;
    stroke-linejoin: round;
  }
  .cloud-outline { fill: var(--ink); }
  .cloud-fill { fill: var(--cloud); }
</style>
</head>
<body>
<svg class="card" viewBox="0 0 1200 741" xmlns="http://www.w3.org/2000/svg">
  <defs>
    <linearGradient id="codeTone" x1="0" y1="0" x2="0" y2="1">
      <stop offset="0" stop-color="var(--code-mid)"/>
      <stop offset="0.3" stop-color="var(--code-dark)"/>
      <stop offset="0.55" stop-color="var(--code-light)"/>
      <stop offset="0.8" stop-color="var(--code-dark)"/>
      <stop offset="1" stop-color="var(--code-mid)"/>
    </linearGradient>
  </defs>

  <rect class="code-backdrop" x="72" y="86" width="1067" height="578" fill="url(#codeTone)"
        role="img" aria-label="Blue binary code pattern background"/>
  <rect class="card-frame" x="72" y="86" width="1067" height="578" fill="none" stroke="var(--frame)" stroke-width="5"/>

  <text class="headline" x="612" y="190" font-size="86" text-anchor="middle" textLength="880" lengthAdjust="spacingAndGlyphs">Technology Help For Seniors</text>

  <!-- thought clouds -->
  <g class="cloud-outline">
    <circle cx="330" cy="295" r="50"/><circle cx="400" cy="280" r="55"/><circle cx="470" cy="300" r="47"/>
    <circle cx="305" cy="360" r="50"/><circle cx="505" cy="355" r="45"/><circle cx="375" cy="375" r="75"/>
    <circle cx="450" cy="385" r="65"/><circle cx="345" cy="440" r="50"/><circle cx="435" cy="445" r="50"/>
    <ellipse cx="400" cy="370" rx="115" ry="100"/>
    <path d="M345 470 L378 566 L415 470 Z"/>
    <rect x="540" y="338" width="100" height="26" rx="13"/>
    <circle cx="675" cy="290" r="60"/><circle cx="765" cy="270" r="60"/><circle cx="845" cy="300" r="55"/>
    <circle cx="655" cy="380" r="60"/><circle cx="885" cy="380" r="55"/><circle cx="760" cy="380" r="105"/>
    <circle cx="715" cy="460" r="60"/><circle cx="815" cy="465" r="60"/>
  </g>
  <g class="cloud-fill">
    <circle cx="330" cy="295" r="45"/><circle cx="400" cy="280" r="50"/><circle cx="470" cy="300" r="42"/>
    <circle cx="305" cy="360" r="45"/><circle cx="505" cy="355" r="40"/><circle cx="375" cy="375" r="70"/>
    <circle cx="450" cy="385" r="60"/><circle cx="345" cy="440" r="45"/><circle cx="435" cy="445" r="45"/>
    <ellipse cx="400" cy="370" rx="110" ry="95"/>
    <path d="M353 466 L378 556 L407 466 Z"/>
    <rect x="540" y="343" width="100" height="16" rx="8"/>
    <circle cx="675" cy="290" r="55"/><circle cx="765" cy="270" r="55"/><circle cx="845" cy="300" r="50"/>
    <circle cx="655" cy="380" r="55"/><circle cx="885" cy="380" r="50"/><circle cx="760" cy="380" r="100"/>
    <circle cx="715" cy="460" r="55"/><circle cx="815" cy="465" r="55"/>
  </g>

  <!-- services -->
  <text class="service" font-size="22" transform="translate(322 262) rotate(38)">E-Readers</text>
  <text class="service" font-size="22" transform="translate(420 275) rotate(55)">E-Mail</text>
  <text class="service" font-size="22" transform="translate(292 315) rotate(45)">Tablets</text>
  <text class="service" font-size="22" x="368" y="368">Mobile Phones</text>
  <text class="service" font-size="22" transform="translate(314 408) rotate(5)">Internet</text>
  <text class="service" font-size="22" transform="translate(400 458) rotate(-25)">Computers</text>

  <text class="service" font-size="32" x="610" y="368">No Question Is</text>
  <text class="service" font-size="32" x="712" y="420">To Small</text>

  <text class="headline" x="608" y="615" font-size="86" text-anchor="middle" textLength="950" lengthAdjust="spacingAndGlyphs">Tech Along, Keep Along</text>
</svg>
</body>
</html>
```